Building company buisness cards

We are looking for a sharp modern new look for our business cards.
We are a New Zealand based company that specialises in house and land packages.
We have attached a photo of the current logo and would like to see if it can be improved somehow if needed.
We are open to any colours but we have chosen green at this stage.
Feel free to change the font and make the logo smarter looking.
Play with the colours and see what looks best.

We want a card that looks so good know one will want to throw it away!

Target Market(s)

Home buyers

Industry/Entity Type

Building

Contact Information for Business Card

Dorian Keswick
0217392604
dkeswick@tidewellhomecraft.co.nz
tidewellhomecraft.co.nz

Font styles to use
Serif
Sans Serif

Colors

Designer to choose colors to be used in the design.

Requirements
Must have
• Logo and company name on one side, details on the other side
Nice to have
• Color codes for the original green are HEX #4a8028, RGB(74,128,40), CMYK(42,0,69,50)
• Round corners, Raised and/or spot UV

```html
<!DOCTYPE html>
<html lang="en">
<head>
<meta charset="utf-8">
<title>Tidewell Homecraft – Business Card</title>
<link href="https://fonts.googleapis.com/css2?family=Open+Sans:wght@400&display=swap" rel="stylesheet">
<style>
  :root {
    --page-bg: #e9e6e1;
    --card-green: #22b60f;
    --card-green-dark: #189a08;
    --circle-white: #ffffff;
    --circle-edge: #f2f2f2;
    --ring-black: #111111;
    --brand-green: #2e9e1f;
    --text-dark: #1a1a1a;
    --rule-grey: #c9c9c9;
  }
  * { margin: 0; padding: 0; box-sizing: border-box; }
  html, body {
    width: 1200px; height: 1024px; overflow: hidden;
    background: var(--page-bg);
  }
  .stage {
    width: 1200px; height: 1024px;
    display: flex; align-items: center; justify-content: center;
  }
  .business-card {
    position: relative;
    width: 900px; height: 520px;
    border-radius: 14px;
    overflow: hidden;
    background: linear-gradient(135deg, var(--card-green) 0%, var(--card-green-dark) 100%);
    box-shadow: 0 18px 40px rgba(0,0,0,0.25);
  }
  .card-circle { position: absolute; inset: 0; }
  .card-content {
    position: absolute; inset: 0;
    display: flex; flex-direction: column; align-items: center; justify-content: center;
    font-family: "Open Sans", sans-serif;
    font-weight: 400;
    text-align: center;
  }
  .company-name {
    display: flex; align-items: center; gap: 14px;
    color: var(--brand-green);
    font-size: 40px;
    line-height: 1.2;
  }
  .company-dot {
    width: 22px; height: 22px; border-radius: 50%;
    background: var(--brand-green);
    flex: none;
  }
  .brand-rule {
    width: 200px; height: 1px;
    background: var(--rule-grey);
    margin: 26px 0 20px;
  }
  .person-name {
    color: var(--text-dark);
    font-size: 30px;
    margin-bottom: 20px;
  }
  .contact-line {
    color: var(--text-dark);
    font-size: 19px;
    line-height: 1.35;
  }
  .contact-line.phone { margin-bottom: 14px; }
</style>
</head>
<body>
<main class="stage">
  <article class="business-card">
    <svg class="card-circle" width="900" height="520" viewBox="0 0 900 520" aria-hidden="true">
      <circle cx="450" cy="260" r="345" fill="var(--circle-white)"/>
      <circle cx="442" cy="268" r="334" fill="var(--ring-black)"/>
      <circle cx="452" cy="258" r="328" fill="var(--circle-edge)"/>
      <circle cx="452" cy="258" r="322" fill="var(--circle-white)"/>
    </svg>
    <div class="card-content">
      <div class="company-name">
        <span class="company-dot"></span>
        <span>Tidewell Homecraft</span>
      </div>
      <div class="brand-rule"></div>
      <p class="person-name">Dorian Keswick</p>
      <p class="contact-line phone">0217392604</p>
      <p class="contact-line">dkeswick@tidewellhomecraft.co.nz</p>
      <p class="contact-line">tidewellhomecraft.co.nz</p>
    </div>
  </article>
</main>
</body>
</html>
```